KRV Construction Management -Business card design request- Lioness black and white shema ONLY - No

It is a woman on construction company I would like the schema to be in black-and-white with the lioness and possibly a lion anulinus as me and my husband both kind of running I would like to see designs for both. Original art would be preferred but like I said I'm going to attach some pictures that I really like and also if you could check my website out that would be great.Please get very creative this is a very important company I will be combining quality construction services with quality construction company and community affiliates such as Halvick construction exedra I really need to show dominates all I'm really wanting is the black-and-white montre and the lioness image on the right side as you will see in some of the thumbnails from what I have had in the past it is OK but I can't connect with anything. These are the last of my advertising dollars I ask that you really please put some time and help me take my company it to the next century. This is going to be a global thing it will be very serious. I'm not trying to be arrogant I'm just trying to tell the truth I ask that you give me something of quality that something that I can put on folders billboards pains walking to places and that it's not that I'm a woman own business but I deftly want there to be A-line as and please play around with the image of the lion and lioness as my husband is a lot of the construction side and I have a decided if Im going to advertise that are notJmsconstructionmanagement.comJovanna Schlossenberg C.E.O.KRV Construction Management Marisela@jmsconstructionmanagement.com81.316.0990

Target Market(s)

Construction or management style. Understand theme ports of marketing and that this logo will be displayed on billboards D cows apps all across the country

Industry/Entity Type

Construction Company

Contact Information for Business Card

Marisela Vandertook
C.E.O.

Marisela@krvconstructionmanagement.example

Www.krvconstructionmanagement.example

729.584.1437

If you can I would like my slogan on their connecting qualify construction services with qualified construction companies and community affiliates

Font styles to use
Sans Serif

Colors
ffffff

Requirements
Must have
• Black-and-white schema lioness on the back side I will list my services will get to that but for now I wanna get the logo design I very open to where you maneuver the contact information
• Marisela Vandertook
• C.E.O.
• Marisela@krvconstructionmanagement.example
• Www.krvconstructionmanagement.example
• 729.584.1437
• If you can I would like my slogan on their connecting qualified construction services with qualified construction companies and community affiliates
Nice to have
• Everything I mentioned above.
• I have added a few pictures with a lion and Linus and know this may seem crazy but I do not like that they are facing to the left I would rather the lion and lioness looked to the right and face forward. Also all the images need to be in black-and-white have provided some color want but I'd like them change to sepia .
Should not have
• I do not want it to look like a cartoon I need this to be of the utmost professionalism

```html
<!DOCTYPE html>
<html lang="en">
<head>
<meta charset="utf-8">
<title>KRV Construction Management – Business Card</title>
<link rel="stylesheet" href="https://fonts.googleapis.com/css2?family=Roboto+Condensed:wght@300;400&family=Exo+2:ital,wght@1,400&display=swap">
<style>
  :root {
    --paper: #ffffff;
    --frame: #8a8a8a;
    --ink-dark: #2b2b2b;
    --ink-mid: #5a5a5a;
    --accent: #c2185b;
    --art-light: #f4f4f4;
    --art-mid: #d6d6d6;
    --art-dark: #9c9c9c;
  }
  * { margin: 0; padding: 0; box-sizing: border-box; }
  html, body {
    width: 1200px;
    height: 747px;
    overflow: hidden;
    background: var(--paper);
  }
  .card {
    position: relative;
    width: 1200px;
    height: 747px;
    background: var(--paper);
    font-family: "Roboto Condensed", sans-serif;
  }
  .card-frame {
    position: absolute;
    left: 60px;
    top: 50px;
    width: 1089px;
    height: 640px;
    border: 2px solid var(--frame);
    overflow: hidden;
  }
  .lioness-art {
    position: absolute;
    left: 560px;
    top: 0;
    width: 527px;
    height: 636px;
    background: radial-gradient(ellipse at 62% 48%, var(--art-light) 0%, var(--art-mid) 55%, var(--art-dark) 100%);
    clip-path: path("M60 0 C20 120 30 260 70 380 C100 470 110 560 120 636 L527 636 L527 0 Z");
  }
  .brand {
    position: absolute;
    left: 170px;
    top: 122px;
    display: flex;
    align-items: center;
    gap: 14px;
  }
  .brand-dot {
    width: 64px;
    height: 64px;
    border-radius: 50%;
    background: var(--accent);
  }
  .brand-name {
    font-family: "Roboto Condensed", sans-serif;
    font-weight: 400;
    font-size: 31px;
    color: var(--ink-dark);
    white-space: nowrap;
  }
  .contact {
    position: absolute;
    left: 0;
    width: 601px;
    text-align: right;
    color: var(--ink-mid);
    font-weight: 300;
    font-size: 26px;
    line-height: 1;
    white-space: nowrap;
  }
  .contact.company { top: 209px; }
  .contact.street  { top: 249px; }
  .contact.city    { top: 285px; }
  .contact.phone   { top: 324px; }
  .contact.email   { top: 361px; font-size: 24px; }
  .contact.web     { top: 393px; font-size: 24px; }
  .person-name {
    position: absolute;
    left: 0;
    width: 603px;
    top: 452px;
    text-align: right;
    font-size: 48px;
    font-weight: 400;
    letter-spacing: -0.5px;
    color: var(--ink-dark);
    line-height: 1;
  }
  .person-title {
    position: absolute;
    left: 0;
    width: 601px;
    top: 511px;
    text-align: right;
    font-size: 24px;
    font-weight: 300;
    letter-spacing: 2px;
    color: var(--ink-mid);
    line-height: 1;
  }
  .slogan {
    position: absolute;
    left: 0;
    width: 601px;
    top: 566px;
    text-align: right;
    font-family: "Exo 2", sans-serif;
    font-style: italic;
    font-size: 24px;
    line-height: 29px;
    color: var(--accent);
  }
</style>
</head>
<body>
<div class="card">
  <div class="card-frame">
    <div class="lioness-art" role="img" aria-label="Grey line-art illustration of a lioness looking forward, filling the right side of the card"></div>
  </div>

  <div class="brand">
    <span class="brand-dot"></span>
    <span class="brand-name">KRV Construction Management</span>
  </div>

  <p class="contact company">Keystone Ventures LLC</p>
  <p class="contact street">2705 NW 61st St Riverton,</p>
  <p class="contact city">MO 64390 US</p>
  <p class="contact phone">Ph:&nbsp; 729.584.1437</p>
  <p class="contact email">Email:&nbsp; Marisela@krvconstructionmanagement.example</p>
  <p class="contact web">Website: Www.krvconstructionmanagement.example</p>

  <h1 class="person-name">Marisela Vandertook</h1>
  <p class="person-title">C.E.O.</p>

  <p class="slogan">connecting qualify construction services<br>with qualified construction companies<br>and community affiliates</p>
</div>
</body>
</html>
```